To create online free mini games website. There’re will be up to 100 games on website with 6-8 categories. Domain name is not selected yet.

Number of Pages Required

1 page

```html
<!DOCTYPE html>
<html lang="en">
<head>
<meta charset="utf-8">
<title>Tobin Games</title>
<link href="https://fonts.googleapis.com/css2?family=Roboto+Condensed:wght@400;700;900&family=Open+Sans:wght@400&display=swap" rel="stylesheet">
<style>
:root{
  --black:#000;
  --white:#fff;
  --gold:#e0b21c;
  --page-bg:#eeeeee;
  --panel-line:#d6d6d6;
  --footer:#141414;
  --muted:#bdbdbd;
  --social:#3d6fb8;
  --head:"Roboto Condensed", Arial, sans-serif;
  --body:"Open Sans", Arial, sans-serif;
}
*{box-sizing:border-box;margin:0;padding:0}
html,body{width:840px;height:1200px;overflow:hidden}
body{position:relative;background:var(--page-bg);font-family:var(--head);color:var(--black)}

.hero{position:absolute;left:0;top:0;width:840px;height:370px;
  background:radial-gradient(ellipse at 50% 40%,#4b3a6b 0%,#2a2340 45%,#120f1c 100%)}
.hero-art{position:absolute;inset:0;
  background:radial-gradient(ellipse at 25% 80%,rgba(90,60,130,.7),transparent 55%),
             radial-gradient(ellipse at 75% 85%,rgba(140,60,160,.6),transparent 50%),
             radial-gradient(ellipse at 60% 15%,rgba(60,70,120,.6),transparent 55%)}
.brand{position:absolute;left:0;top:150px;width:840px;text-align:center;
  font-family:var(--head);font-weight:900;color:var(--gold);line-height:.9}
.brand .name{display:block;font-size:92px;letter-spacing:-1px}
.brand .sub{display:block;font-size:58px}

.main-nav{position:absolute;left:0;top:370px;width:840px;height:47px;background:var(--black);
  display:flex;align-items:center;padding-left:73px}
.main-nav a{color:var(--white);text-decoration:none;font-size:15px;letter-spacing:.5px;margin-right:23px}
.search{position:absolute;left:646px;top:380px;width:122px;height:21px;border-bottom:1px solid #555;
  display:flex;justify-content:space-between;align-items:center;color:#999;font-size:10px;font-family:var(--body)}

.content{position:absolute;left:60px;top:417px;width:720px;height:637px;background:var(--white);
  box-shadow:0 0 18px rgba(0,0,0,.25)}

.bar{position:absolute;height:37px;background:var(--black);color:var(--white);
  font-size:18px;font-weight:400;display:flex;align-items:center;padding-left:9px;letter-spacing:.3px}
.bar.center{justify-content:center;padding-left:0}

.tile-row{position:absolute;left:73px;width:480px;height:116px;display:flex;justify-content:space-between}
.tile{width:113px;height:116px;background:var(--black);display:flex;flex-direction:column}
.tile .art{height:86px;background:var(--art)}
.tile .label{flex:1;color:var(--white);font-size:13px;display:flex;align-items:center;justify-content:center}

.tabs{position:absolute;left:73px;top:849px;width:480px;height:21px;display:flex;gap:3px}
.tabs span{flex:1;border:1px solid #333;font-size:11px;display:flex;align-items:center;justify-content:center}

.card{position:absolute;left:570px;width:198px;background:#f4f4f4;border:1px solid var(--panel-line);border-top:none}
.daily{top:475px;height:159px;background:var(--white)}
.daily .art{position:absolute;left:4px;top:5px;width:188px;height:150px;
  background:radial-gradient(circle at 50% 45%,#2aa6d6 0%,#116a9a 55%,#0a3c66 100%)}
.recent{top:684px;height:206px}
.recent .item{position:absolute;left:4px;width:82px;height:60px;background:var(--art)}
.recent .title{position:absolute;left:106px;font-size:13px}
.tagbox{top:936px;height:58px}
.tag{position:absolute;width:48px;height:15px;border:1px solid #333;font-size:7px;
  display:flex;align-items:center;justify-content:center;background:var(--white)}

.footer{position:absolute;left:0;top:1054px;width:840px;height:146px;background:var(--footer)}
.social{position:absolute;top:1090px;left:346px;display:flex;gap:7px}
.social span{width:23px;height:23px;border-radius:50%;background:var(--social)}
.footer-links{position:absolute;top:1126px;left:0;width:840px;text-align:center;
  font-family:var(--body);font-size:11px;color:var(--white)}
.footer-links i{font-style:normal;margin:0 13px;color:#aaa}
.copyright{position:absolute;top:1152px;left:0;width:840px;text-align:center;
  font-family:var(--body);font-size:10px;color:var(--muted)}
</style>
</head>
<body>

<header class="hero">
  <div class="hero-art" role="img" aria-label="Fantasy scene with a dragon above a glowing crystal cave"></div>
  <div class="brand"><span class="name">TOBIN</span><span class="sub">games</span></div>
</header>

<nav class="main-nav">
  <a href="#">Action</a><a href="#">Casino</a><a href="#">Adventure</a><a href="#">Puzzle</a><a href="#">Driving</a><a href="#">Sports</a><a href="#">Bubble</a>
</nav>
<div class="search"><span>Search</span>
  <svg width="9" height="9" viewBox="0 0 10 10"><circle cx="4" cy="4" r="3" fill="none" stroke="#e0a21c" stroke-width="1.5"/><line x1="6.2" y1="6.2" x2="9" y2="9" stroke="#e0a21c" stroke-width="1.5"/></svg>
</div>

<main class="content"></main>

<div class="bar" style="left:73px;top:438px;width:480px">EDITOR'S PICK</div>
<section class="tile-row" style="top:482px">
  <div class="tile"><div class="art" role="img" aria-label="Explorer holding a torch in a cave" style="--art:linear-gradient(160deg,#b07a3a,#3a2512)"></div><div class="label">GAME 1</div></div>
  <div class="tile"><div class="art" role="img" aria-label="Platform game level with floating islands" style="--art:linear-gradient(#8fd3f0 0%,#8fd3f0 45%,#6a3a22 46%,#3a1d10 100%)"></div><div class="label">GAME 1</div></div>
  <div class="tile"><div class="art" role="img" aria-label="Runner crossing a bridge at dusk" style="--art:linear-gradient(#3b4ea0,#d49bb8 60%,#2a2340)"></div><div class="label">GAME 1</div></div>
  <div class="tile"><div class="art" role="img" aria-label="Colourful doodle pattern of cartoon objects" style="--art:linear-gradient(135deg,#f2cf2e,#e2a21a)"></div><div class="label">GAME 1</div></div>
</section>

<div class="bar" style="left:73px;top:638px;width:480px">HOT GAMES</div>
<section class="tile-row" style="top:683px">
  <div class="tile"><div class="art" role="img" aria-label="Maze puzzle in outer space" style="--art:linear-gradient(135deg,#2a3f8a,#f0b640 55%,#1c2a66)"></div><div class="label">GAME 1</div></div>
  <div class="tile"><div class="art" role="img" aria-label="Platform level with coins and bridges" style="--art:linear-gradient(#a8e2f2 0%,#a8e2f2 30%,#4a3142 31%,#2d1e2a 100%)"></div><div class="label">GAME 1</div></div>
  <div class="tile"><div class="art" role="img" aria-label="Football on a stadium pitch under a scoreboard" style="--art:linear-gradient(#0c1c3a,#1a4a7a 50%,#1d6a2a)"></div><div class="label">GAME 1</div></div>
  <div class="tile"><div class="art" role="img" aria-label="Tournament group table on green" style="--art:linear-gradient(#1f9a3a,#0f6a25)"></div><div class="label">GAME 1</div></div>
</section>

<div class="tabs"><span>ACTION</span><span>CASINO</span><span>ADVENTURE</span><span>PUZZLE</span><span>DRIVING</span><span>SPORTS</span><span>BUBBLE</span></div>
<section class="tile-row" style="top:876px">
  <div class="tile"><div class="art" role="img" aria-label="Golden slot jackpot with coins" style="--art:radial-gradient(circle,#e8b32a,#a0171a 70%)"></div><div class="label">GAME 1</div></div>
  <div class="tile"><div class="art" role="img" aria-label="Top-down town map with roads" style="--art:linear-gradient(135deg,#8ad0e8,#5fa8c8)"></div><div class="label">GAME 1</div></div>
  <div class="tile"><div class="art" role="img" aria-label="Treasure map on a wooden table" style="--art:linear-gradient(135deg,#f0a531,#d6831c)"></div><div class="label">GAME 1</div></div>
  <div class="tile"><div class="art" role="img" aria-label="White sports car on a city highway" style="--art:linear-gradient(#cfd6dc,#8a9096)"></div><div class="label">GAME 1</div></div>
</section>

<aside>
  <div class="bar center" style="left:570px;top:438px;width:198px">GAME OF DAY</div>
  <div class="card daily"><div class="art" role="img" aria-label="Casino promo with jackpot slot machine and roulette"></div></div>

  <div class="bar center" style="left:570px;top:646px;width:198px">RECENTLY VISITED</div>
  <div class="card recent">
    <div class="item" role="img" aria-label="Pixel street scene with game over banner" style="top:6px;--art:linear-gradient(#c9b3d6,#7a6a8a)"></div><div class="title" style="top:28px">GAME 1</div>
    <div class="item" role="img" aria-label="Brick platform level with trees" style="top:74px;--art:linear-gradient(#9ed6f0,#d1703a)"></div><div class="title" style="top:96px">GAME 1</div>
    <div class="item" role="img" aria-label="Children on a rainbow among clouds" style="top:141px;--art:linear-gradient(#9ad8f2,#e6d450)"></div><div class="title" style="top:163px">GAME 1</div>
  </div>

  <div class="bar center" style="left:570px;top:898px;width:198px">TAGS</div>
  <div class="card tagbox">
    <span class="tag" style="left:11px;top:10px">ACTION</span>
    <span class="tag" style="left:65px;top:10px">CASINO</span>
    <span class="tag" style="left:119px;top:10px">BUBBLE</span>
    <span class="tag" style="left:11px;top:31px">ADVENTURE</span>
    <span class="tag" style="left:65px;top:31px">PUZZLE</span>
    <span class="tag" style="left:119px;top:31px">DRIVING</span>
  </div>
</aside>

<footer class="footer"></footer>
<div class="social"><span></span><span></span><span></span><span></span><span></span></div>
<div class="footer-links">About Us<i>|</i>Contact Us<i>|</i>Terms &amp; Conditions</div>
<div class="copyright">©2018 Tobin Games. All Rights Reserved.</div>

</body>
</html>
```